Booklet Design needed for Copperleaf Digital Studio

A Little bit about us:
At Copperleaf Digital Studio we offer our clients the very best in their website needs without the big price tag.

We take the hassle out of setting up a website and take care of the website design, domain registration, SEO and hosting.
We know how important it is to have a Visually Appealing website, that’s why when we are designing our websites we focus on the main things like branding, content, creativity, colors, layout, ease of use, and imagery.

Design Specifics:
I currently have two booklets that I give to my clients:
one before I start designing their site as a general information booklet
and the other one I give only once I complete their site - which is about how to use my editor.

I want to jazz these two booklets up and bit with a modern and professional look, and I want both the booklets to have a similar design, I would also like it to be a similar look to my website, www.copperleafdigitalstudio.com.au.

Previously the budget was AUD$130. Now it is AUD$260.
This reflects your creative effort for 2 booklets.

I have uploaded the two booklets, labeled Booklet 1 (7 pages) and Booklet 2 (15 pages), inside you will find the information and images I want on each page.
The booklets also need a title page.

Thanks Designers. Will appreciate all your creative effort!

Hi Designers . i have updated the content for one of the booklets. the new file which i will upload shortly is called "New Client information Booklet content update". please use this for one of the booklets to be designed. the other booklet still needs to be done (the one with the editor information inside)Cheers Added Thursday, October 29, 2015

Target Market(s)

Small to medium Businesses

Font styles to use
Sans Serif

Colors
3176b5
5c5c5c
ffffff

Requirements
Must have
• Logo, images and content from original booklets. And the Seperate booklets for the two different booklets. Similar modern, professional design.
Nice to have
• Moder, professional design, similar look to my website. Www.copperleafdigitalstudio.com.au

```html
<!DOCTYPE html>
<html lang="en">
<head>
<meta charset="utf-8">
<title>General Information – Copperleaf Digital Studio</title>
<link href="https://fonts.googleapis.com/css2?family=Alegreya+Sans:wght@400;500&display=swap" rel="stylesheet">
<style>
  :root {
    --brand-blue: #3176b5;
    --heading-blue: #2f6db1;
    --ink: #5c5c5c;
    --ink-dark: #4a4a4a;
    --rule: #6a6a6a;
    --paper: #ffffff;
    --band-dark: #1d2630;
  }
  * { box-sizing: border-box; margin: 0; padding: 0; }
  html, body { width: 928px; height: 1200px; overflow: hidden; background: var(--paper); }
  body { font-family: "Alegreya Sans", sans-serif; color: var(--ink-dark); }
  .page { position: relative; width: 928px; height: 1200px; background: var(--paper); }
  .header-band {
    position: absolute; left: 0; top: 0; width: 100%; height: 84px;
    background: linear-gradient(to bottom, var(--band-dark) 0%, #2a5e95 22%, #6b9ccc 55%, #ffffff 100%);
  }
  .page-title {
    position: absolute; left: 94px; top: 90px;
    font-size: 64px; font-weight: 400; color: var(--heading-blue); line-height: 1;
  }
  .rule { position: absolute; left: 95px; width: 770px; height: 1.5px; background: var(--rule); }
  .section-title {
    position: absolute; left: 94px;
    font-size: 46px; font-weight: 400; color: var(--ink-dark); line-height: 1;
  }
  .body-text {
    position: absolute; left: 95px; width: 770px;
    font-size: 16.6px; line-height: 21.6px; color: var(--ink-dark); text-align: justify;
  }
  .contact-line { font-size: 16.6px; }
  .contact-line a { color: var(--brand-blue); text-decoration: none; margin-left: 4px; }
  .callout {
    position: absolute; left: 84px; top: 567px; width: 782px; height: 78px;
    border-radius: 12px; background: var(--paper);
    box-shadow: 0 0 8px rgba(49,118,181,0.28);
    display: flex; align-items: center; justify-content: center; padding: 0 12px;
    text-align: center; color: var(--brand-blue); font-size: 16.6px; line-height: 21.6px;
  }
  .footer-bar { position: absolute; left: 84px; top: 1135px; width: 772px; height: 5px; display: flex; }
  .footer-bar .blue { width: 568px; background: var(--brand-blue); }
  .footer-bar .grey { flex: 1; background: var(--ink-dark); }
  .page-number {
    position: absolute; right: 72px; top: 1148px;
    font-size: 16.6px; color: var(--ink-dark);
  }
</style>
</head>
<body>
<div class="page">
  <div class="header-band"></div>

  <h1 class="page-title">General Information</h1>
  <div class="rule" style="top:164px"></div>
  <h2 class="section-title" style="top:170px">Website maintance</h2>

  <p class="body-text" style="top:257px">At Copperleaf Digital Studio we provide our clients the very best in their website need and we will continue to provide support to all our existing and new clients.</p>
  <p class="body-text" style="top:320px">As you are a Premium customer you will receive premium support. With premium Support we offer support, with no charge, to all our clients for assistance with their website, so if you are having trouble with your website or have any questions please contact us.</p>
  <p class="body-text" style="top:411px">We also offer general maintenance for our clients, free for most of our premium customers. We can update information and add any content to your website. We only charge a small fee for general website maintenance.</p>
  <p class="body-text contact-line" style="top:496px">FOR SUPPORT CONTACT - <a href="mailto:support@copperleafdigitalstudio.com.au">support@copperleafdigitalstudio.com.au</a></p>

  <div class="callout">On our website under the support page we also have support videos with using our editor, you may also find<br>these helpful along with this booklet.</div>

  <div class="rule" style="top:735px"></div>
  <h2 class="section-title" style="top:747px">About the editor</h2>

  <p class="body-text" style="top:863px">Our website hosting is a rock solid web host that is hosted by our datacentre redundant, cloud based hosting infrastructure.</p>
  <p class="body-text" style="top:920px">Client's websites live in multiple data centres locations to offer superior up-time, response time, and reliability compared to most any other hosting option.</p>
  <p class="body-text" style="top:994px">On Website that we design we offer unlimited storage and unlimited bandwidth hosting.</p>

  <div class="footer-bar"><span class="blue"></span><span class="grey"></span></div>
  <div class="page-number">Page 01</div>
</div>
</body>
</html>
```